Business Card Design Project

I am looking for a minimal matte background/shiny (spot UV) ink monochromatic design with a splash of neon color.

the card should be 2 sided, logo only on one side - all info and possibly logo on the other.

My creative director described the colors he imagined for the design to be:
'it's a dark field, like charcoal or a really dark burgundy, or deep blue, shot through with a neon—but just a tiny bit of it. so a charcoal field with a laser-thin streak of electric lime, safety orange, or cobalt blue. really beautiful stuff.'

here are some samples of the types of cards I am trying to create:
http://www.snapvault.example/photos/dawnpress/4182736450/in/photostream -> Vornelle Lustre

http://www.snapvault.example/photos/dawnpress/3859201746/in/photostream -> Standard Coated (14pt/matte) with SPOT UV

http://www.snapvault.example/photos/dawnpress/3859201372/in/photostream/ -> Dense Orvane with Raised Ink

http://www.snapvault.example/photos/dawnpress/5128463907/in/photostream/ -> Standard Coated (14pt/matte) with SPOT UV

Here is my logo:
https://www.filecrate.example/s/qtrwx730pkd4zn/gulvane%20logotype%20final.ai

Here are the details for info:
Owen Carlisle Dray
email - owen@gulvane.example
mobile - 555 318 6724
web -
gulvane.example: inventive technology applications
gulvane-video.example: innovative video advertising

please let me know if there is anything at all that you need.

Target Market(s)

mid to large agencies that require interactive design and entrepreneurial/startup individuals/companies that need application development.

Industry/Entity Type

Safety

Requirements
Must have
• logo only on one side

```html
<!DOCTYPE html>
<html lang="en">
<head>
<meta charset="utf-8">
<title>Gulvane — Business Card</title>
<link href="https://fonts.googleapis.com/css2?family=Open+Sans:wght@300;400&display=swap" rel="stylesheet">
<style>
  :root {
    --backdrop: #eaeceb;
    --card: #35343a;
    --ink: #b8b8bd;
    --tick: #d4d4d8;
    --cobalt: #1b78bf;
  }
  * { margin: 0; padding: 0; box-sizing: border-box; }
  html, body {
    width: 1200px;
    height: 900px;
    overflow: hidden;
    background: var(--backdrop);
  }
  .canvas {
    position: relative;
    width: 1200px;
    height: 900px;
  }
  .card {
    position: absolute;
    width: 560px;
    height: 320px;
    background: var(--card);
  }
  .card--front { left: 70px; top: 110px; }
  .card--back { left: 570px; top: 470px; }

  .wordmark {
    position: absolute;
    left: 50%;
    top: 50%;
    transform: translate(-50%, -50%);
    display: flex;
    align-items: center;
    gap: 10px;
  }
  .wordmark__name {
    font-family: "Open Sans", sans-serif;
    font-weight: 400;
    font-size: 34px;
    letter-spacing: 0.32em;
    color: var(--cobalt);
  }
  .wordmark__dot {
    width: 10px;
    height: 10px;
    border-radius: 50%;
    background: var(--cobalt);
    margin-top: -22px;
  }

  .details {
    position: absolute;
    left: 130px;
    top: 150px;
    list-style: none;
    font-family: "Open Sans", sans-serif;
    font-weight: 300;
    font-size: 12.5px;
    line-height: 17px;
    color: var(--ink);
  }
  .details__line {
    position: relative;
    padding-left: 22px;
  }
  .details__line::before {
    content: "";
    position: absolute;
    background: var(--tick);
  }
  .details__line--bar::before {
    left: 4px;
    top: 3px;
    width: 1.5px;
    height: 11px;
  }
  .details__line--dash::before {
    left: 0;
    top: 14px;
    width: 11px;
    height: 1.5px;
  }
</style>
</head>
<body>
  <main class="canvas">
    <section class="card card--front" aria-label="Card front">
      <div class="wordmark">
        <span class="wordmark__name">GULVANE</span>
        <span class="wordmark__dot"></span>
      </div>
    </section>

    <section class="card card--back" aria-label="Card back">
      <ul class="details">
        <li class="details__line details__line--bar">Owen Carlisle Dray</li>
        <li class="details__line details__line--dash">email - owen@gulvane.example</li>
        <li class="details__line details__line--bar">mobile - 555 318 6724</li>
        <li class="details__line details__line--dash">web - www.gulvane.example</li>
        <li class="details__line details__line--bar">gulvane.example: inventive technology applications</li>
        <li class="details__line details__line--dash">gulvane-video.example: innovative video advertising</li>
      </ul>
    </section>
  </main>
</body>
</html>
```